Industry automation wholesale website

www.velqora.eu provides solutions for automation, building automation and digital signage.

Our products are rugged, reliable, energy saving and representative.

Scope of pages:
● welcome page
- scope of products
- applications, success stories and news
● category page
- short introduction
- sub categories
- product highlights
● product page
- short introduction
- about 3 to 4 pictures
- technical specifications: materials, dimensions
- price
- related products

Optional:
● contact page
- address
- contact form
● blog
- picture
- text
● logo
● favicon / apple touch icon

Conclusion:
● We need a professionally looking site
● Bright colors (e.g. white, grey, metalic colors, blue)

some pages we like:
http://www.brundafel.de/
http://www.korvimash.de/

Target Market(s)

Our target market is the industrial sector
● Target audience: engineering and IT professionals

Industry/Entity Type

Building

Requirements
Must have
• ● only use free available fonts e.g. Pellor Type Library (http://www.pellortype.com/webfonts)
Should not have
• ● sound
● flash

```html
<!DOCTYPE html>
<html lang="en">
<head>
<meta charset="utf-8">
<title>Velqora – Industrial Automation</title>
<link rel="stylesheet" href="https://fonts.googleapis.com/css2?family=Montserrat:wght@400;600;700&family=Roboto+Slab:wght@400;700&display=swap">
<style>
  :root {
    --brand-blue: #1b86bd;
    --brand-deep: #17659a;
    --nav-text: #4a4f55;
    --util-text: #2f95c8;
    --hero-light: #8fd3ea;
    --hero-mid: #62b7d8;
    --hero-dark: #3f93b8;
    --about-bg: #e1f3fb;
    --body-text: #3d4145;
    --white: #ffffff;
    --rule: #d6dde2;
  }
  * { margin: 0; padding: 0; box-sizing: border-box; }
  html, body { width: 1200px; height: 900px; overflow: hidden; background: var(--about-bg); }
  body { position: relative; font-family: "Roboto Slab", Georgia, serif; }

  .top-band { position: absolute; left: 0; top: 0; width: 1200px; height: 7px;
    background: linear-gradient(90deg, var(--brand-deep), var(--brand-blue) 45%, #6cc6ea); }

  .site-header { position: absolute; left: 0; top: 7px; width: 1200px; height: 170px; background: var(--white); }

  .utility-bar { position: absolute; right: 48px; top: 14px; display: flex; align-items: center;
    font-family: "Montserrat", Arial, sans-serif; font-size: 10px; color: var(--util-text); }
  .utility-bar span { padding: 0 14px; border-left: 1px solid var(--rule); line-height: 18px; display: flex; align-items: center; gap: 7px; }
  .utility-bar span:first-child { border-left: none; }
  .utility-bar .caret { width: 0; height: 0; border-left: 4px solid transparent; border-right: 4px solid transparent; border-top: 5px solid var(--util-text); }

  .brand { position: absolute; left: 39px; top: 60px; display: flex; align-items: center; gap: 12px;
    font-family: "Montserrat", Arial, sans-serif; font-weight: 400; font-size: 40px; color: var(--brand-deep); letter-spacing: 0.5px; }
  .brand .mark { width: 14px; height: 14px; border-radius: 50%; background: var(--brand-deep); }

  .main-nav { position: absolute; top: 96px; left: 0; width: 1200px; height: 30px;
    font-family: "Montserrat", Arial, sans-serif; font-size: 10.5px; font-weight: 600; letter-spacing: 0.6px; color: var(--nav-text); }
  .main-nav a { position: absolute; top: 8px; text-decoration: none; color: inherit; white-space: nowrap; }
  .main-nav a.active { color: var(--brand-blue); font-weight: 700; }
  .main-nav .search { position: absolute; left: 1132px; top: 6px; }
  .nav-indicator { position: absolute; left: 611px; top: 165px; width: 64px; height: 5px; background: var(--brand-blue); }

  .hero { position: absolute; left: 0; top: 177px; width: 1200px; height: 432px; overflow: hidden; }
  .hero-photo { position: absolute; inset: 0;
    background: linear-gradient(100deg, var(--hero-light) 0%, var(--hero-mid) 40%, var(--hero-dark) 75%, var(--hero-mid) 100%); }
  .hero-shade { position: absolute; inset: 0;
    background: linear-gradient(180deg, rgba(255,255,255,0.08), rgba(30,110,150,0.18)); }
  .hero-content { position: absolute; left: 0; top: 140px; width: 1200px; text-align: center; color: var(--white); }
  .hero-content svg { display: block; margin: 0 auto 30px; }
  .hero-content h1 { font-size: 23px; font-weight: 700; line-height: 30px; }
  .slider-arrow { position: absolute; top: 188px; width: 46px; height: 44px; background: rgba(255,255,255,0.9);
    display: flex; align-items: center; justify-content: center; }
  .slider-arrow.prev { left: 0; }
  .slider-arrow.next { right: 0; }

  .about { position: absolute; left: 0; top: 609px; width: 1200px; height: 291px; background: var(--about-bg); text-align: center; }
  .about h2 { margin-top: 112px; font-size: 22px; font-weight: 400; color: var(--brand-blue); letter-spacing: 0.5px; }
  .about p { width: 800px; margin: 22px auto 0; font-size: 14.5px; line-height: 24px; color: var(--body-text); }
</style>
</head>
<body>
  <div class="top-band"></div>

  <header class="site-header">
    <div class="utility-bar">
      <span>Sign Out</span>
      <span>My Account <i class="caret"></i></span>
      <span>English <i class="caret"></i></span>
      <span>
        <svg width="14" height="11" viewBox="0 0 14 11" fill="none" stroke="currentColor" stroke-width="1.2"><path d="M0.5 1h2l1.8 6h7l1.6-4.5H3.4"/><circle cx="5.5" cy="9.3" r="0.9"/><circle cx="10" cy="9.3" r="0.9"/></svg>
        0€
      </span>
    </div>

    <div class="brand"><i class="mark"></i>velqora</div>

    <nav class="main-nav">
      <a class="active" style="left:626px">HOME</a>
      <a style="left:694px">PRODUCTS</a>
      <a style="left:784px">APPLICATIONS</a>
      <a style="left:890px">SUPPORT</a>
      <a style="left:970px">ABOUT US</a>
      <a style="left:1051px">CONTACT</a>
      <svg class="search" width="14" height="14" viewBox="0 0 14 14" fill="none" stroke="#4a4f55" stroke-width="1.6"><circle cx="5.8" cy="5.8" r="4.3"/><path d="M9 9l4 4"/></svg>
    </nav>
  </header>
  <div class="nav-indicator"></div>

  <section class="hero">
    <div class="hero-photo" role="img" aria-label="Blue-tinted photo of people walking through a bright modern office lobby"></div>
    <div class="hero-shade"></div>
    <div class="hero-content">
      <svg width="72" height="56" viewBox="0 0 72 56" fill="none" stroke="#ffffff" stroke-width="5">
        <rect x="3" y="3" width="66" height="38"/>
        <path d="M36 41v8M22 53h28" stroke-linecap="square"/>
      </svg>
      <h1>Velqora is your specialist partner<br>for industrial automation.</h1>
    </div>
    <div class="slider-arrow prev">
      <svg width="10" height="14" viewBox="0 0 10 14" fill="none" stroke="#1b86bd" stroke-width="2.4"><path d="M7 2L3 7l4 5"/></svg>
    </div>
    <div class="slider-arrow next">
      <svg width="10" height="14" viewBox="0 0 10 14" fill="none" stroke="#1b86bd" stroke-width="2.4"><path d="M3 2l4 5-4 5"/></svg>
    </div>
  </section>

  <section class="about">
    <h2>ABOUT US</h2>
    <p>Eum ex, laoreet iudicabit posid onium quo te. Mei ex legere civibus phaedrum. Id eam putent conceptam.
      Ad malis nihil epicurei dolorum torquatos ut, cu prolegere civibus phaedrum. Id eam putent conceptam movet
      debitis graecis.Eum ex, laoreet iudicabit posid onium quo te. Mei ex legere civibus phaedrum. Id eam putent
      conceptam. Ad malis nihil epicurei dolorum torquatos ut, cu prolegere civibus phaedrum.</p>
  </section>
</body>
</html>
```